Want to fly? Flight school needs a roll up

Hello designers

We are a small aviation club with around 100 members. We love flying and therefore offer free flight lessons for young people at our glider flight school.
The young people only have to pay a flat rate of €300 for the aircraft until their first solo flight.
To advertise the flight school we now need a roll up banner measuring 85cm x 200cm. You can find the data sheet for the banner in the appendix.
Content of the roll up banner:
Advertising for our flight school so that we can attract new members
The banner should be designed in our club colors blue/white
The banner is aimed at all people who want to get a glider license
A great offer for young people up to the age of 25 should be placed on the banner with a reference to the text “Offer only applies to people up to the age of 25. Included in the flat rate of €300 is training on the glider up to the first "solo flight"
The banner is intended to advertise training with a glider. Therefore the wish would be for a glider to be depicted

Here is a link to our current homepage

https://www.lsg-tarnhofen.de/

https://www.vidoplex.example/watch?v=K8p2Qz4LmXc

Target Market(s)

Young people from 14 years to 30 years

Colors
0054AA
0677BA
7BADD7
CADEEF
E8F1F8

Requirements
Nice to have
• Glider / club logo
Should not have
• Too much text

```html
<!DOCTYPE html>
<html lang="en">
<head>
<meta charset="utf-8">
<title>Glider Licence Roll-up – Luftsportgruppe Tarnhofen e.V.</title>
<link rel="stylesheet" href="https://fonts.googleapis.com/css2?family=Outfit:ital,wght@0,400;0,500;0,800;1,400&display=swap">
<style>
  :root {
    --club-navy: #2b3590;
    --club-ink: #1f2a86;
    --plane-blue: #3a7fd6;
    --plane-deep: #1d4fa0;
    --paper: #ffffff;
    --stage: #ececec;
  }
  * { box-sizing: border-box; margin: 0; padding: 0; }
  html, body {
    width: 1200px;
    height: 1200px;
    overflow: hidden;
    background: var(--stage);
    font-family: "Outfit", sans-serif;
  }
  .rollup {
    position: absolute;
    left: 360px;
    top: 35px;
    width: 480px;
    height: 1130px;
    background: var(--paper);
    overflow: hidden;
  }
  .club-mark {
    position: absolute;
    top: 95px;
    left: 0;
    width: 100%;
    display: flex;
    flex-direction: column;
    align-items: center;
    gap: 16px;
  }
  .club-mark__dot {
    width: 120px;
    height: 120px;
    border: 5px solid var(--club-ink);
    border-radius: 50%;
  }
  .club-mark__name {
    color: var(--club-ink);
    font-weight: 500;
    font-size: 20px;
    text-align: center;
    line-height: 1.25;
  }
  .sky {
    position: absolute;
    inset: 0;
    width: 480px;
    height: 1130px;
  }
  .sky path { fill: var(--club-navy); }
  .glider-art {
    position: absolute;
    left: 33px;
    top: 462px;
    width: 405px;
    height: 150px;
    border-radius: 28px;
    background: linear-gradient(135deg, var(--plane-blue), var(--plane-deep));
  }
  .offer {
    position: absolute;
    left: 0;
    top: 718px;
    width: 100%;
    text-align: center;
    color: var(--paper);
  }
  .offer__headline {
    font-weight: 800;
    font-size: 42px;
    line-height: 1.08;
    letter-spacing: 0.3px;
    text-transform: uppercase;
  }
  .offer__age {
    position: absolute;
    left: 38px;
    top: 132px;
    width: 402px;
    height: 108px;
    background: var(--paper);
    border-radius: 48% 52% 45% 55% / 55% 50% 50% 45%;
    color: var(--club-ink);
    font-size: 24px;
    line-height: 1.3;
    display: flex;
    align-items: center;
    justify-content: center;
    text-align: center;
  }
  .offer__price {
    position: absolute;
    left: 0;
    top: 278px;
    width: 100%;
    font-size: 24px;
    line-height: 1.3;
  }
  .offer__price strong { font-weight: 500; font-size: 30px; }
</style>
</head>
<body>
  <main class="rollup">
    <div class="club-mark">
      <span class="club-mark__dot"></span>
      <span class="club-mark__name">Luftsportgruppe<br>Tarnhofen e.V.</span>
    </div>

    <svg class="sky" viewBox="0 0 480 1130" aria-hidden="true">
      <path d="M0,1130 L0,690 Q10,650 55,658 Q70,615 120,625 Q150,590 195,612 Q220,585 255,600
               L300,560 Q285,515 330,500 Q318,450 370,440 Q380,398 425,405 Q445,378 480,392 L480,1130 Z"/>
    </svg>

    <div class="glider-art" role="img" aria-label="Illustration of a blue aircraft climbing above the clouds"></div>

    <section class="offer">
      <h1 class="offer__headline">Get<br>a glider license</h1>
      <p class="offer__age">Offer only applies to people<br>up to the age of 25</p>
      <p class="offer__price">Flat rate of <strong>€300</strong><br>is training on the glider<br>up to the first "<em>solo flight</em>"</p>
    </section>
  </main>
</body>
</html>
```